Portal Panel Medic need professional looking business card printed on plastic, Commericial, Industri

We are family owned and operated garage door company in Indianapolis, Indiana. We sale service and install dock equipment, doors, operators. We are looking to expand our commercial/ industrial division. We also service all residential doors and operators. We are looking for a business that stands out of the crowd. We are committed to have the best customer service in the industry.

Target Market(s)

National and local general contractors, National/ Corpate service accounts,

Industry/Entity Type

Business Service

Contact Information for Business Card

To be printed on plastic stock

Font styles to use
Sans Serif

Colors
ffffff
f04a50
ec1f27

Requirements
Must have
• Name, website,email, phone number, position.
Nice to have
• A standout professional design

```html
<!DOCTYPE html>
<html lang="en">
<head>
<meta charset="utf-8">
<title>Portal Panel Medic – Business Card</title>
<link href="https://fonts.googleapis.com/css2?family=Open+Sans:wght@400&family=Libre+Baskerville:wght@400&display=swap" rel="stylesheet">
<style>
  :root {
    --white: #ffffff;
    --red: #ec1f27;
    --red-soft: #f04a50;
    --black: #101010;
    --black-hi: #2c2c2c;
    --stage: #e9e6e2;
    --muted: #d9d9d9;
  }
  * { box-sizing: border-box; margin: 0; padding: 0; }
  html, body { width: 1200px; height: 996px; overflow: hidden; }
  body {
    background: var(--stage);
    font-family: "Open Sans", Arial, sans-serif;
    position: relative;
  }
  .card {
    position: absolute;
    width: 620px;
    height: 354px;
    border-radius: 4px;
    overflow: hidden;
    box-shadow: 0 10px 28px rgba(0,0,0,.22);
  }
  .card--front { left: 70px; top: 90px; background: var(--black); }
  .card--back {
    left: 510px; top: 550px;
    background: linear-gradient(120deg, var(--black) 0%, var(--black-hi) 48%, var(--black) 100%);
    display: flex; align-items: center; justify-content: center;
  }
  .front__top {
    position: absolute; left: 0; top: 0; width: 100%; height: 172px;
    background: var(--white);
    display: flex; align-items: center; justify-content: center;
  }
  .wordmark {
    display: flex; align-items: center; gap: 12px;
    font-family: "Libre Baskerville", Georgia, serif;
    font-weight: 400;
    font-size: 28px;
    line-height: 1;
  }
  .front__top .wordmark { color: var(--black); }
  .card--back .wordmark { color: var(--white); }
  .wordmark__dot {
    width: 14px; height: 14px; border-radius: 50%; background: var(--red);
  }
  .identity {
    position: absolute; left: 40px; top: 205px; width: 260px;
    text-align: right; color: var(--white);
  }
  .identity__name {
    font-family: "Libre Baskerville", Georgia, serif;
    font-size: 25px; line-height: 1.2;
  }
  .identity__role {
    font-family: "Libre Baskerville", Georgia, serif;
    font-size: 22px; line-height: 1.3;
  }
  .identity__address {
    margin-top: 12px; font-size: 13px; line-height: 1.55; color: var(--muted);
  }
  .contacts {
    position: absolute; left: 336px; top: 200px; list-style: none;
  }
  .contacts__item {
    display: flex; align-items: center; gap: 14px;
    height: 31px; color: var(--white); font-size: 14px;
  }
  .contacts__icon {
    width: 22px; height: 22px; border-radius: 50%;
    background: var(--white);
    display: flex; align-items: center; justify-content: center;
    flex: none;
  }
  .contacts__icon svg { width: 13px; height: 13px; }
</style>
</head>
<body>

<section class="card card--front" aria-label="Business card front">
  <div class="front__top">
    <div class="wordmark"><span class="wordmark__dot"></span>Portal Panel Medic</div>
  </div>

  <div class="identity">
    <p class="identity__name">Marcus Hollin</p>
    <p class="identity__role">Managing Director</p>
    <p class="identity__address">1234,Address GoesHere<br>Country,12345</p>
  </div>

  <ul class="contacts">
    <li class="contacts__item">
      <span class="contacts__icon"><svg viewBox="0 0 24 24"><path fill="#ec1f27" d="M6.6 10.8a15.1 15.1 0 0 0 6.6 6.6l2.2-2.2a1 1 0 0 1 1-.25 11.4 11.4 0 0 0 3.6.57 1 1 0 0 1 1 1V20a1 1 0 0 1-1 1A17 17 0 0 1 3 4a1 1 0 0 1 1-1h3.5a1 1 0 0 1 1 1c0 1.25.2 2.450.57 3.6a1 1 0 0 1-.25 1z"/></svg></span>
      123-456-789
    </li>
    <li class="contacts__item">
      <span class="contacts__icon"><svg viewBox="0 0 24 24"><path fill="#ec1f27" d="M6.6 10.8a15.1 15.1 0 0 0 6.6 6.6l2.2-2.2a1 1 0 0 1 1-.25 11.4 11.4 0 0 0 3.6.57 1 1 0 0 1 1 1V20a1 1 0 0 1-1 1A17 17 0 0 1 3 4a1 1 0 0 1 1-1h3.5a1 1 0 0 1 1 1c0 1.25.2 2.45.57 3.6a1 1 0 0 1-.25 1z"/></svg></span>
      123-456-789
    </li>
    <li class="contacts__item">
      <span class="contacts__icon"><svg viewBox="0 0 24 24"><rect x="2" y="5" width="20" height="14" rx="1.5" fill="#ec1f27"/><path d="M3 6l9 7 9-7" fill="none" stroke="#fff" stroke-width="1.8"/></svg></span>
      info@youremail.com
    </li>
    <li class="contacts__item">
      <span class="contacts__icon"><svg viewBox="0 0 24 24"><circle cx="12" cy="12" r="9" fill="none" stroke="#ec1f27" stroke-width="2"/><path d="M3 12h18M12 3c3 3 3 15 0 18M12 3c-3 3-3 15 0 18" fill="none" stroke="#ec1f27" stroke-width="1.6"/></svg></span>
      www.yourweb.com
    </li>
  </ul>
</section>

<section class="card card--back" aria-label="Business card back">
  <div class="wordmark"><span class="wordmark__dot"></span>Portal Panel Medic</div>
</section>

</body>
</html>
```